WordPress design project for Verlani Construction

Verlani Construction, Inc. (www.verlaniinc.example) is a private organization. It is run by the same family that founded Verlani Refuse Systems (www.verlani.example), a large, publicly-held waste management organization in the US. While owned by the same family, the two organizations are run independently.
Verlani Construction is a well-established New England USA construction outfit specializing in site development, heavy excavation, aggregate, large-scale/municipal water and sewer systems, and landfill construction and closure. Verlani Construction is not in any way a residential or commercial building contractor.
Verlani Construction also operates hydraulic and hydrostatic service shops, as well as aggregate (gravel, sand, stone, top soil, and anything else aggregate) sites. Both are for more traditional, non-project customers, such as landscapers and other construction companies.
Business contact information is as noted below:
Address:
Verlani Construction, Inc.
48 Quarry Ridge Road
Mendon, Vermont 05829
Telephone:
802-555-0147
Fax:
802-555-0183
Email:
info@verlaniinc.example
A tagline used in a recent advertisement was:
"Committed to providing a complete array of services for over 30 years, we are New England's premier construction company."
In reviewing design ideas internally, we found bits and pieces of the following sites appealing:
RT Construction (Dorwenski) - http://www.rtconstruction.example/
Halbrook Construction - http://www.halbrook.example/
Pelham Construction - http://www.pelhamconstruction.example/
Riverbend Construction Group - http://www.riverbendconstructiongroup.example/
Krage Construction - http://www.krage.example/
Vail Sisters Construction http://www.vailsis.example/
Tolliver Construction http://www.tolliver-corp.example/
The blue in the logo is hex #00253f. The logo was designed by hand many years ago, so the font is unknown.
We would like a fresh, professional design that effectively illustrates what we do in a thoughtful, impressive way.
Target Market(s)
Would-be clients, land developers, waste organizations, energy developers, engineers, surveyors, landscapers, heavy equipment operators and the likes.
Industry/Entity Type
Waste Management
Requirements
Must have
- Lots of media capabilities, such as embedded video (via YouTube is fine), project image gallery, and sliders for various functions.
A large slider on the landing page is critical, as well as space for standard things, such as news/events, job opportunities, project highlights, and the likes.
We also want to highlight things like employee longevity. Some of our team have been with us since the beginning.
We need to add emphasis to the fact that our hydraulic/hydro static services and aggregate operations are for anyone who needs such service or material. Related, we need a place to set prices and descriptions of such material to help site visitors decide what they may need.
We need a place to highlight business partners, such as Amos Fairley and Gruntwell.
We also need form capabilities for things like bid requests and general contacts from the public. Related, there should be social media capabilities.
Nice to have
- This is almost a must have, but we're open to options. The WordPress design should be capable of fitting into the very popular PlumPages Easel theme.

```html
<!DOCTYPE html>
<html lang="en">
<head>
<meta charset="utf-8">
<title>Verlani Construction</title>
<link href="https://fonts.googleapis.com/css2?family=Open+Sans:ital,wght@0,400;0,600;0,700;1,600&display=swap" rel="stylesheet">
<style>
:root{
  --navy:#00253f;
  --blue:#1a9ad6;
  --blue-dark:#0f6fa8;
  --blue-soft:#3fb3e6;
  --ink:#2b2f33;
  --muted:#6d757c;
  --line:#d9dee2;
  --panel:#eef1f3;
  --footer:#22292f;
  --footer-deep:#171c20;
  --white:#ffffff;
}
*{box-sizing:border-box;margin:0;padding:0}
html,body{width:1200px;height:2224px;overflow:hidden}
body{position:relative;background:var(--white);font-family:"Open Sans",Arial,sans-serif;color:var(--ink);font-size:13px}
.abs{position:absolute}
.container{position:absolute;left:150px;width:900px}

/* top strip */
.top-strip{top:0;left:0;width:1200px;height:40px;background:var(--navy)}
.top-contacts{left:150px;top:12px;display:flex;gap:26px;color:#cfe3f0;font-size:11px}
.top-contacts span{display:flex;align-items:center;gap:6px}
.logo-box{left:430px;top:0;width:240px;height:120px;background:var(--white);box-shadow:0 2px 8px rgba(0,0,0,.25);display:flex;align-items:center;justify-content:center;gap:10px;padding:0 14px}
.logo-mark{width:16px;height:16px;background:var(--navy);flex:none}
.logo-name{font-weight:700;font-size:21px;color:var(--navy);line-height:1.1}
.util-links{right:150px;top:48px;font-size:11px;color:var(--muted);display:flex;gap:8px}
.search{right:150px;top:80px;width:200px;height:26px;background:var(--navy);border-radius:3px;color:#9fb6c6;font-size:11px;padding:5px 10px;display:flex;justify-content:space-between;align-items:center}

/* nav */
.main-nav{top:144px;height:46px;background:var(--panel);border-top:1px solid var(--line);border-bottom:1px solid var(--line);display:flex;align-items:stretch}
.main-nav a{display:flex;align-items:center;padding:0 18px;color:var(--navy);font-weight:600;font-size:14px;text-decoration:none}
.main-nav a.active{background:var(--blue);color:var(--white)}

/* hero */
.hero{top:190px;left:0;width:1200px;height:250px;background:linear-gradient(100deg,#1d3a52 0%,#36627f 35%,#7a98ab 65%,#a7b4bb 100%)}
.hero-text{top:232px;left:200px;width:440px;color:var(--white);font-size:27px;font-weight:600;line-height:1.3}
.hero-dots{top:410px;left:1040px;display:flex;gap:6px}
.hero-dots i{width:9px;height:9px;border-radius:50%;background:rgba(255,255,255,.6);display:block}
.hero-dots i.on{background:var(--blue-soft)}

/* section heads */
.section-title{font-size:16px;font-weight:700;color:var(--navy);padding-bottom:8px;border-bottom:2px solid var(--line);position:relative}
.section-title::after{content:"";position:absolute;left:0;bottom:-2px;width:90px;height:2px;background:var(--blue)}
.pager{position:absolute;right:0;top:0;display:flex;gap:4px}
.pager b{width:20px;height:20px;background:#c7ccd0;color:var(--white);font-size:11px;display:flex;align-items:center;justify-content:center}
.pager b.on{background:var(--blue)}

/* projects */
.projects{top:462px}
.project-cards{display:flex;gap:30px;margin-top:22px}
.project-card{width:280px;background:var(--panel);border:1px solid var(--line)}
.project-photo{height:170px;background:linear-gradient(180deg,#5f8fb6 0%,#a9c4d8 60%,#d8e2e8 100%);position:relative}
.project-card.featured .project-photo{background:linear-gradient(180deg,#2a7fb7 0%,#79b3d8 60%,#c5dce9 100%)}
.zoom{position:absolute;left:122px;top:67px;width:36px;height:36px;border-radius:50%;background:var(--blue)}
.project-body{padding:12px 14px 16px}
.project-body h3{font-size:12px;font-weight:700;color:var(--navy);margin-bottom:6px}
.project-body p{font-size:11px;color:var(--muted);line-height:1.45}

/* updates */
.updates{top:960px;height:240px}
.side-menu{position:absolute;left:0;top:0;width:210px;border:1px solid var(--line)}
.side-menu li{list-style:none;height:40px;border-bottom:1px solid var(--line);display:flex;align-items:center;gap:10px;padding-left:14px;font-size:12px;color:var(--navy)}
.side-menu li:last-child{border-bottom:0}
.side-menu li.on{background:var(--panel)}
.side-menu i{width:10px;height:10px;background:var(--blue);display:block}
.video{position:absolute;left:250px;top:0;width:330px;height:200px;background:linear-gradient(135deg,#2c3a44,#55636c);border:4px solid #1c2328}
.play{position:absolute;left:145px;top:78px}
.video-bar{position:absolute;left:0;bottom:0;width:100%;height:20px;background:rgba(0,0,0,.55)}
.update-text{position:absolute;left:610px;top:20px;width:290px}
.update-text h3{font-size:14px;font-weight:700;color:var(--navy);margin-bottom:8px}
.update-text p{font-size:11px;color:var(--muted);line-height:1.55}
.btn{display:inline-block;background:var(--blue);color:var(--white);font-size:12px;font-weight:600;padding:7px 14px;border-radius:3px}
.update-text .btn{position:absolute;right:0;top:170px}

/* services & team */
.services{top:1248px;width:420px;left:150px}
.service-list{margin-top:18px}
.service-item{display:flex;gap:12px;margin-bottom:18px}
.service-item i{flex:none;width:18px;height:18px;border-radius:50%;border:2px solid var(--navy);margin-top:2px;position:relative}
.service-item i::after{content:"";position:absolute;left:4px;top:4px;width:6px;height:6px;border-radius:50%;background:var(--navy)}
.service-item h4{font-size:12px;font-weight:600;color:var(--ink)}
.service-item p{font-size:11px;color:var(--muted);line-height:1.45}
.team{top:1248px;left:630px;width:420px}
.team-photo{position:absolute;left:0;top:46px;width:150px;height:180px;background:linear-gradient(180deg,#e9edf0,#c9d1d7);border:1px solid var(--line)}
.team-text{position:absolute;left:170px;top:52px;width:250px}
.team-text h3{font-size:14px;font-weight:700;color:var(--navy);margin-bottom:8px;line-height:1.3}
.team-text p{font-size:11px;color:var(--muted);line-height:1.5}
.team-text .btn{margin-top:14px;float:right}

/* clients */
.clients{top:1540px}
.client-row{display:flex;align-items:center;gap:16px;margin-top:30px}
.arrow{width:22px;height:40px;display:flex;align-items:center;justify-content:center;color:#9aa3aa;font-size:26px}
.client{width:150px;height:90px;border:1px solid var(--line);display:flex;align-items:center;justify-content:center;font-weight:700;font-size:17px;color:var(--ink)}
.client.hover{border-color:var(--blue)}
.tip{position:absolute;left:334px;top:40px;background:var(--ink);color:var(--white);font-size:10px;padding:3px 8px}

/* testimonial */
.testimonial{top:1730px;left:0;width:1200px;height:76px;background:var(--blue-soft)}
.say{position:absolute;left:150px;top:0;height:76px;width:230px;background:var(--blue);color:var(--white);font-style:italic;font-weight:600;font-size:18px;display:flex;align-items:center;padding-left:18px}
.quote{position:absolute;left:410px;top:18px;width:560px;color:var(--white);font-size:12px;font-style:italic;line-height:1.5}
.t-nav{position:absolute;left:1000px;top:26px;display:flex;gap:4px}
.t-nav b{width:22px;height:22px;background:rgba(255,255,255,.35);color:var(--white);font-size:12px;display:flex;align-items:center;justify-content:center}

/* footer */
.footer{top:1806px;left:0;width:1200px;height:374px;background:var(--footer);color:#b9c2c9}
.footer h5{font-size:12px;font-weight:700;color:var(--white);margin-bottom:14px;letter-spacing:.5px}
.col-industries{position:absolute;left:150px;top:34px;width:220px}
.col-industries li{list-style:none;font-size:11px;height:24px;display:flex;align-items:center;gap:8px}
.col-industries li::before{content:"";width:5px;height:5px;background:var(--blue-soft)}
.col-industries li.on{color:var(--white);text-decoration:underline}
.col-contact{position:absolute;left:420px;top:34px;width:240px;font-size:11px;line-height:1.65}
.col-contact b{color:var(--white);font-weight:600;display:inline-block;width:72px}
.col-form{position:absolute;left:720px;top:34px;width:330px}
.field{display:flex;gap:12px;margin-bottom:12px;font-size:11px}
.field label{width:56px;padding-top:5px}
.field span{flex:1;height:26px;background:#323b42;border:1px solid #3f4950}
.field.tall span{height:110px}
.col-form .btn{margin-left:250px;padding:6px 14px;font-size:11px}
.bottom-bar{top:2180px;left:0;width:1200px;height:44px;background:var(--footer-deep);color:#8d979f;font-size:10px}
.bottom-bar .copy{position:absolute;left:150px;top:15px}
.bottom-bar .links{position:absolute;right:150px;top:15px;display:flex;gap:8px}
</style>
</head>
<body>

<header>
  <div class="abs top-strip"></div>
  <div class="abs top-contacts">
    <span><svg width="12" height="9" viewBox="0 0 12 9"><rect x=".5" y=".5" width="11" height="8" fill="none" stroke="#cfe3f0"/><path d="M.5 .5 6 5l5.5-4.5" fill="none" stroke="#cfe3f0"/></svg>info@verlaniinc.example</span>
    <span><svg width="10" height="10" viewBox="0 0 10 10"><path d="M2 0h2l1 3-1.5 1a6 6 0 0 0 2.5 2.5L7 5l3 1v2c0 1-1 2-2 2A8 8 0 0 1 0 2c0-1 1-2 2-2z" fill="#cfe3f0"/></svg>802-555-0147</span>
    <span><svg width="10" height="10" viewBox="0 0 10 10"><rect x="1" y="3" width="8" height="5" fill="#cfe3f0"/><rect x="3" y="0" width="4" height="3" fill="#cfe3f0"/></svg>802-555-0183</span>
  </div>
  <div class="abs logo-box"><span class="logo-mark"></span><span class="logo-name">Verlani Construction</span></div>
  <nav class="abs util-links"><span>Login</span><span>|</span><span>Newsroom</span><span>|</span><span>Contact Us</span></nav>
  <div class="abs search"><span>Search the site</span><svg width="12" height="12" viewBox="0 0 12 12"><circle cx="5" cy="5" r="3.8" fill="none" stroke="#9fb6c6" stroke-width="1.6"/><path d="m8 8 3 3" stroke="#9fb6c6" stroke-width="1.6"/></svg></div>
  <nav class="container main-nav">
    <a class="active">Home</a><a>Our Work</a><a>Services</a><a>Industries</a><a>Resources</a><a>Our Team</a>
  </nav>
</header>

<section class="abs hero" role="img" aria-label="Slider photo of a construction site with cranes and a rising building under a blue sky"></section>
<p class="abs hero-text">Committed to providing a complete array of services for over 30 years, we are New England's premier construction company.</p>
<div class="abs hero-dots"><i></i><i></i><i class="on"></i></div>

<section class="container projects">
  <h2 class="section-title">Recent Projects</h2>
  <div class="pager"><b>‹</b><b class="on">›</b></div>
  <div class="project-cards">
    <article class="project-card featured">
      <div class="project-photo" role="img" aria-label="Project photo of modern office towers"><span class="zoom"></span></div>
      <div class="project-body"><h3>This is Draftsmith's version of Lorem</h3><p>Lorem. Proin gravida nibh vel velit auctor aliquet. Aenean sollicitudin, lorem quis bibendum.</p></div>
    </article>
    <article class="project-card">
      <div class="project-photo" role="img" aria-label="Project photo of modern office towers"></div>
      <div class="project-body"><h3>This is Draftsmith's version of Lorem</h3><p>Lorem. Proin gravida nibh vel velit auctor aliquet. Aenean sollicitudin, lorem quis bibendum.</p></div>
    </article>
    <article class="project-card">
      <div class="project-photo" role="img" aria-label="Project photo of modern office towers"></div>
      <div class="project-body"><h3>This is Draftsmith's version of Lorem</h3><p>Lorem. Proin gravida nibh vel velit auctor aliquet. Aenean sollicitudin, lorem quis bibendum.</p></div>
    </article>
  </div>
</section>

<section class="container updates">
  <ul class="side-menu">
    <li class="on"><i></i>News/Events</li>
    <li><i></i>Project Highlights</li>
    <li><i></i>Job Opportunity</li>
    <li><i></i>Bid Request</li>
  </ul>
  <div class="video" role="img" aria-label="Embedded video still of heavy equipment at work">
    <svg class="play" width="40" height="40" viewBox="0 0 40 40"><circle cx="20" cy="20" r="19" fill="rgba(255,255,255,.85)"/><path d="M15 11v18l14-9z" fill="#f2b01e"/></svg>
    <div class="video-bar"></div>
  </div>
  <div class="update-text">
    <h3>This is Draftsmith's version of Lorem</h3>
    <p>This is Draftsmith's version of Lorem Ipsum. Proin gravida nibh vel velit auctor aliquet. Aenean sollicitudin, lorem quis bibendum auctor, nisi elit consequat ipsum, nec sagittis sem nibh id elit. Duis sed odio sit amet nibh vulputate cursus.</p>
    <span class="btn">Read More</span>
  </div>
</section>

<section class="abs services">
  <h2 class="section-title">Our Services</h2>
  <div class="service-list">
    <div class="service-item"><i></i><div><h4>This is Draftsmith's version of Lorem Ipsum. Proin</h4><p>gravida nibh vel velit auctor aliquet. Aenean sollicitudin, lorem quis bibendum auctor, nisi elit consequat ipsum, nec sagittis sem nibh id elit.</p></div></div>
    <div class="service-item"><i></i><div><h4>This is Draftsmith's version of Lorem Ipsum. Proin</h4><p>gravida nibh vel velit auctor aliquet. Aenean sollicitudin, lorem quis bibendum auctor, nisi elit consequat ipsum, nec sagittis sem nibh id elit.</p></div></div>
    <div class="service-item"><i></i><div><h4>This is Draftsmith's version of Lorem Ipsum. Proin</h4><p>gravida nibh vel velit auctor aliquet. Aenean sollicitudin, lorem quis bibendum auctor, nisi elit consequat ipsum, nec sagittis sem nibh id elit.</p></div></div>
  </div>
</section>

<section class="abs team">
  <h2 class="section-title">Our Team</h2>
  <div class="pager"><b>‹</b><b class="on">›</b></div>
  <div class="team-photo" role="img" aria-label="Portrait photo of a smiling team member in business attire"></div>
  <div class="team-text">
    <h3>This is Draftsmith's version of Lorem</h3>
    <p>This is Draftsmith's version of Lorem Ipsum. Proin gravida nibh vel velit auctor aliquet. Aenean sollicitudin, lorem quis bibendum auctor, nisi elit consequat ipsum, nec sagittis sem nibh id elit.</p>
    <span class="btn">Read More</span>
  </div>
</section>

<section class="container clients">
  <h2 class="section-title">Our Clients</h2>
  <span class="tip">Amos Fairley</span>
  <div class="client-row">
    <span class="arrow">‹</span>
    <div class="client">Gruntwell</div>
    <div class="client hover">Amos Fairley</div>
    <div class="client">Gruntwell</div>
    <div class="client">Amos Fairley</div>
    <div class="client">Gruntwell</div>
    <span class="arrow">›</span>
  </div>
</section>

<section class="abs testimonial">
  <div class="say">What customers say?</div>
  <p class="quote">“ This is Draftsmith's version of Lorem Ipsum. Proin gravida nibh vel velit auctor aliquet. Aenean sollicitudin, lorem quis bibendum auctor, nisi elit consequat ipsum. ”</p>
  <div class="t-nav"><b>‹</b><b>›</b></div>
</section>

<footer class="abs footer">
  <div class="col-industries">
    <h5>INDUSTRIES WE SERVE</h5>
    <ul>
      <li>Education</li><li>Food &amp; Retail</li><li class="on">Hospitals</li><li>Industrial</li><li>Sustainability Services</li>
      <li>Renewables</li><li>Construction</li><li>Multi-Location Accounts</li><li>Airports</li><li>Government</li>
    </ul>
  </div>
  <div class="col-contact">
    <h5>CONTACT INFO</h5>
    <p><b>Address:</b></p>
    <p>Verlani Construction, Inc.<br>48 Quarry Ridge Road<br>Mendon, Vermont 05829</p>
    <p style="margin-top:10px"><b>Telephone:</b>802-555-0147</p>
    <p><b>Fax:</b>802-555-0183</p>
    <p><b>Email:</b>info@verlaniinc.example</p>
  </div>
  <div class="col-form">
    <h5>CONTACT US</h5>
    <div class="field"><label>Name</label><span></span></div>
    <div class="field"><label>Email</label><span></span></div>
    <div class="field tall"><label>Message</label><span></span></div>
    <span class="btn">SUBMIT</span>
  </div>
</footer>

<div class="abs bottom-bar">
  <span class="copy">© 2008-2014 Verlani Construction, Inc. All Rights Reserved.</span>
  <nav class="links"><span>Home</span>|<span>Sitemap</span>|<span>Careers</span>|<span>Contact Us</span>|<span>Investor Relations</span>|<span>E-Pay</span>|<span>Privacy Policy</span></nav>
</div>

</body>
</html>
```